Business Card - Rebranding for Consulting Firm

We are renaming and rebranding our consulting firm and need to raise the level of quality of our cards as part of that effort. We consult to leading high tech, life science and other innovation sector companies.

Need a two-sided business card design.

Side 1: (a) Company logo (b) tag line: Sharpen the Return on Your People (c) Name (d) Title (e) Phone 1: Office (f) Phone 2: Mobile (g) email: person@HollowmereAdvisory.com

Side 2: Two lines of text: (a) Markets Shift Daily. Teams Adapt Quickly. People Deliver the Plan. (b) We guide you through all three.

Target Market(s)

Business and human resources executives and senior managers

Industry/Entity Type

Management Consulting

Contact Information for Business Card

Font styles to use
Sans Serif

Requirements
Must have
• clean, not too busy, but with a bit of creativity. Stick to the colors used in the attached logo
• appeal to high tech, life science companies
Nice to have
• prefer white background

```html
<!DOCTYPE html>
<html lang="en">
<head>
<meta charset="utf-8">
<title>Hollowmere Advisory – Business Card</title>
<link href="https://fonts.googleapis.com/css2?family=Arimo:wght@400;700&display=swap" rel="stylesheet">
<style>
  :root {
    --brand-blue: #1c6aa6;
    --ink: #3a3a3a;
    --paper: #ffffff;
    --backdrop: #e4e6e8;
    --rule: #9a9a9a;
  }
  * { box-sizing: border-box; margin: 0; padding: 0; }
  html, body {
    width: 1200px; height: 1200px; overflow: hidden;
    background: var(--backdrop);
    font-family: "Arimo", Arial, sans-serif;
  }
  .canvas {
    width: 1200px; height: 1200px;
    display: flex; flex-direction: column; align-items: center; justify-content: center;
    gap: 60px;
  }
  .card {
    position: relative;
    width: 900px; height: 514px;
    box-shadow: 0 6px 18px rgba(0,0,0,0.18);
    overflow: hidden;
  }

  /* Front */
  .card-front { background: var(--paper); }
  .brand {
    position: absolute; left: 200px; top: 38px;
    display: flex; align-items: center; gap: 14px;
  }
  .brand-mark { width: 30px; height: 30px; background: var(--brand-blue); }
  .brand-name {
    font-size: 50px; font-weight: 400; color: var(--brand-blue);
    letter-spacing: -0.5px; white-space: nowrap; line-height: 1;
  }
  .identity {
    position: absolute; right: 482px; top: 244px; text-align: right;
  }
  .identity-name { font-size: 34px; color: var(--brand-blue); white-space: nowrap; }
  .identity-title { font-size: 18px; color: var(--ink); margin-top: 8px; }
  .divider {
    position: absolute; left: 444px; top: 222px; width: 2px; height: 148px;
    background: var(--rule);
  }
  .contacts {
    position: absolute; left: 464px; top: 226px; list-style: none;
  }
  .contact {
    display: flex; align-items: center; gap: 14px;
    height: 48px; font-size: 18px; color: var(--ink); white-space: nowrap;
  }
  .contact svg { width: 24px; height: 24px; fill: var(--ink); flex: none; }
  .tagline-band {
    position: absolute; left: 0; right: 0; bottom: 0; height: 34px;
    background: var(--brand-blue);
    display: flex; align-items: center; justify-content: center;
    color: #fff; font-size: 16px;
  }

  /* Back */
  .card-back { background: var(--brand-blue); color: #fff; }
  .statement {
    position: absolute; left: 0; right: 0; top: 214px;
    text-align: center; font-size: 24px; white-space: nowrap;
  }
  .promise-row {
    position: absolute; left: 0; right: 0; top: 266px;
    display: flex; align-items: center; justify-content: center; gap: 20px;
  }
  .promise-rule { width: 238px; height: 6px; border-radius: 3px; background: #fff; }
  .promise { font-size: 20px; white-space: nowrap; }
</style>
</head>
<body>
<main class="canvas">

  <section class="card card-front" aria-label="Business card front">
    <div class="brand">
      <span class="brand-mark"></span>
      <span class="brand-name">Hollowmere Advisory</span>
    </div>

    <div class="identity">
      <div class="identity-name">Daniel R. Okafor</div>
      <div class="identity-title">Managing Director</div>
    </div>

    <div class="divider"></div>

    <ul class="contacts">
      <li class="contact">
        <svg viewBox="0 0 24 24" aria-label="Office phone"><path d="M3 8c0-2 2-4 9-4s9 2 9 4v2h-4V8H7v2H3V8zm3 4h12l2 8H4l2-8zm6 1.5a3 3 0 1 0 0 6 3 3 0 0 0 0-6z"/></svg>
        <span>555-014-2286</span>
      </li>
      <li class="contact">
        <svg viewBox="0 0 24 24" aria-label="Mobile phone"><path d="M6.6 10.8a15.1 15.1 0 0 0 6.6 6.6l2.2-2.2a1 1 0 0 1 1-.25 11.4 11.4 0 0 0 3.6.57 1 1 0 0 1 1 1V20a1 1 0 0 1-1 1A17 17 0 0 1 3 4a1 1 0 0 1 1-1h3.5a1 1 0 0 1 1 1c0 1.250.2 2.450.57 3.570a1 1 0 0 1-.25 1z"/></svg>
        <span>555-017-4431</span>
      </li>
      <li class="contact">
        <svg viewBox="0 0 24 24" aria-label="Email"><path d="M2 5h20v14H2V5zm2 2v.4l8 5.2 8-5.2V7H4zm0 2.8V17h16V9.8l-8 5.2-8-5.2z"/></svg>
        <span>person@HollowmereAdvisory.com</span>
      </li>
    </ul>

    <div class="tagline-band">Sharpen the Return on Your People</div>
  </section>

  <section class="card card-back" aria-label="Business card back">
    <p class="statement">Markets Shift Daily. Teams Adapt Quickly. People Deliver the Plan</p>
    <div class="promise-row">
      <span class="promise-rule"></span>
      <p class="promise">We guide you through all three</p>
      <span class="promise-rule"></span>
    </div>
  </section>

</main>
</body>
</html>
```